Private Equity Company Stationary
business card, letterhead, envelope, fax cover
#46 please eliminate the email address from the envelope. Thanks
#34 Birchway Holdings Group Header and remove big logo/watermark from the center of the page.
#33 remove all the phone numbers from envelope
#21 please eliminate border (header and footer) from business card, letterhead, fax coverand just leave it plain. Please re-submit with changes
envelope flaps to remain white
The only place the cell phone number is needed is on the business card.
I need some clarification before I can submit a satifactory design.
1. Do we need to mention the name "Holdings Grouup Advisory, Inc." compulsarily in any of the media.
2. Are there any limitations on the no of colours that can be used as printing costs can vary significantly.

```html
<!DOCTYPE html>
<html lang="en">
<head>
<meta charset="utf-8">
<title>Birchway Holdings – Business Card</title>
<link rel="stylesheet" href="https://fonts.googleapis.com/css2?family=Tinos:wght@400&display=swap">
<style>
  :root {
    --navy: #1f3f73;
    --tan: #8b7a5c;
    --paper: #ffffff;
    --rule: #9a8a6c;
  }
  html, body {
    margin: 0;
    padding: 0;
    width: 1200px;
    height: 754px;
    overflow: hidden;
    background: var(--paper);
  }
  .card {
    position: relative;
    width: 1200px;
    height: 754px;
    background: var(--paper);
    font-family: "Tinos", "Times New Roman", serif;
    overflow: hidden;
  }
  .brand {
    position: absolute;
    left: 40px;
    top: 58px;
    display: flex;
    align-items: center;
  }
  .brand-mark {
    width: 34px;
    height: 34px;
    background: var(--navy);
  }
  .brand-divider {
    width: 2px;
    height: 110px;
    background: var(--rule);
    margin: 0 22px 0 26px;
  }
  .brand-name {
    font-size: 44px;
    color: var(--navy);
    letter-spacing: 0.5px;
    white-space: nowrap;
  }
  .holder {
    position: absolute;
    right: 25px;
    top: 72px;
    text-align: right;
  }
  .holder-name {
    font-size: 50px;
    color: var(--navy);
    line-height: 1;
    letter-spacing: 0.5px;
    white-space: nowrap;
  }
  .holder-title {
    font-size: 40px;
    color: var(--tan);
    margin-top: 12px;
    line-height: 1;
  }
  .contact {
    position: absolute;
    right: 25px;
    top: 440px;
    text-align: right;
    font-size: 35px;
    line-height: 57px;
    color: var(--tan);
    white-space: nowrap;
    font-style: normal;
  }
  .contact .value { color: var(--navy); }
  .bands {
    position: absolute;
    left: 0;
    top: 600px;
  }
</style>
</head>
<body>
  <main class="card">
    <header class="brand">
      <div class="brand-mark"></div>
      <div class="brand-divider"></div>
      <div class="brand-name">BIRCHWAY HOLDINGS</div>
    </header>

    <section class="holder">
      <div class="holder-name">DANIEL VALMORENT</div>
      <div class="holder-title">Managing Director</div>
    </section>

    <address class="contact">
      <div class="value">214 W Harlow Ave, Suite 480, Los Angeles, CA 90028</div>
      <div>Phone: <span class="value">(310) 555-0142</span>, Cell: <span class="value">(310) 555-0187</span>, Fax: <span class="value">(310) 555-0163</span></div>
      <div>E-mail: <span class="value">daniel@birchwayhg.com</span>, website: <span class="value">www.birchwayhg.com</span></div>
    </address>

    <svg class="bands" width="1200" height="80" viewBox="0 0 1200 80" aria-hidden="true">
      <rect class="band-navy" x="170" y="14" width="1030" height="20" fill="var(--navy)"/>
      <rect class="band-tan" x="80" y="48" width="1120" height="20" fill="var(--tan)"/>
    </svg>
  </main>
</body>
</html>
```